依頼詳細
PCとスマホデザインの両方納品をいただきますが、
まずはデザインイメージが確認しやすいPCページのみの提案をお願いします。
スマホページは当選者に納品時にお願いしたいと思います。
スマホサイズについて、カンバスサイズは横幅375pxで作成し、2倍の横幅750pxのサイズで書き出ししてください。
(Retinaディスプレイに対応するため)
スマホページ作成時は、メニューが展開した際のデザインもお願いします。
レスポンシブウェブデザインを意識したデザインでお願いします。

■サイトマップ
添付の画面遷移図をご確認ください。

■参考サイト
・サイトの雰囲気・イメージの参考サイト
https://mosvelu.jp/
・掲載製品の詳細
https://www.tovilka.co.jp/brand/palomix.html

■内容について
以下のサイトのリニューアルになります。
http://kuraden-shelf.jp/
倉庫ラックを製造していることと製品自体を紹介し、見積り依頼へアクションを促すサイトになります。
・公式サイト
https://www.hoben-tk.jp/

■素材写真
画像データについては、フリー素材から流用して
イメージ画像に当て込んでください。
足りない場合は、一旦他のサイトの写真をサンプルとして
入れてください。(サンプルなどの表記をお願いします)
また、購入が必要な写真などを利用した場合、
価格とサイト名を教えてください。

また、Adobe Stockで定期契約をしていますので、
Adobe Stockの画像は使用できます。
デザイン時はカンプ画像をお入れいただきますようお願いします。

■ワイヤーフレーム
https://wire.plenora.example/view/c39e27f0-5b1d-4a8e-9f62-b71d0e5a3c28-ab7d/?fullscreen
コンテンツの構成としてワイヤーフレームを作成しましたが
必ずしもワイヤーフレームの通りではなくて大丈夫です。
TOPページに配置するコンテンツを見ていただき、デザインは
デザイナーの皆様におまかせしたいと思います。

----------------------------------------------------------------------------
【制作物に対するお願い】

■フォントについて
・無料で使えるフォントで作成をお願いします。
・OSに紐づくフォントの使用は控えていただければと思います (ヒラギノなど)

■メインビジュアルについて
メインビジュアルは今のところスライドの予定です。
可能であれば以下の内容でメインビジュアルも作成していただきたいです。
①パロミクスについての紹介
②特価品のキャンペーン(今まで作成していた倉庫ラックを特価で販売する、といった内容)
③受注生産なので色やサイズなど色々カスタマイズ可能

シンプル 複雑
単色 カラフル
暗い 明るい
日常 高級
遊び心 厳粛
未来的 伝統的
女性的 男性的
ベースカラー:白、ポイントカラー:濃い目の緑(公式サイトのカラー)
• 高解像度JPG (.jpg)
• イラストレーター形式 (.ai)
• フォトショップ形式 (.psd)
上記のいずれか1つ(アウトラインありとなしの2つ)と高解像度JPGを納品お願いします。
adobe XDでの納品も可能です。

```html
<!DOCTYPE html>
<html lang="ja">
<head>
<meta charset="utf-8">
<title>宝辺製作所 | パロミクス</title>
<link rel="stylesheet" href="https://fonts.googleapis.com/css2?family=Noto+Sans+JP:wght@400;500;700;900&family=Oswald:wght@500;700&display=swap">
<style>
:root{
  --green:#1f6b4f;
  --green-dark:#174f3b;
  --sage:#8c9a7d;
  --beige:#efe9e1;
  --ink:#222;
  --dark:#1e1e1e;
  --red:#c8282e;
  --white:#fff;
  --line:#ddd;
  --muted:#777;
}
*{box-sizing:border-box;margin:0;padding:0}
html,body{width:1200px;height:4692px;overflow:hidden}
body{font-family:"Noto Sans JP",sans-serif;color:var(--ink);background:var(--white);position:relative}
section,header,footer{position:absolute;left:0;width:1200px;overflow:hidden}
.photo{position:absolute}
.en{font-family:"Oswald",sans-serif;letter-spacing:.04em}
.plus{display:inline-flex;width:26px;height:26px;background:var(--green);color:#fff;align-items:center;justify-content:center;font-weight:700;font-size:18px;line-height:1}

/* header */
.site-header{top:0;height:110px;background:#fff;display:flex;align-items:center}
.brand{position:absolute;left:32px;top:34px;display:flex;align-items:center;gap:10px;font-weight:900;font-size:26px;color:var(--green)}
.brand-mark{width:34px;height:34px;background:var(--green)}
.brand small{font-size:12px;display:block;line-height:1;margin-bottom:2px}
.gnav{position:absolute;left:390px;top:36px;display:flex;gap:46px}
.gnav li{list-style:none;font-size:14px;font-weight:700;text-align:center}
.gnav li span{display:block;font-size:9px;color:var(--muted);font-weight:400;margin-top:4px}
.dropdown{position:absolute;left:485px;top:82px;background:#fff;padding:12px 16px;font-size:12px;font-weight:700;line-height:2;z-index:3;box-shadow:0 4px 10px rgba(0,0,0,.08)}
.header-cta{position:absolute;right:0;top:0;display:flex;height:100px}
.header-cta a{width:116px;color:#fff;font-size:13px;font-weight:700;text-decoration:none;display:flex;flex-direction:column;align-items:center;justify-content:center;gap:8px}
.header-cta a:first-child{background:var(--green)}
.header-cta a:last-child{background:var(--green-dark)}
.header-cta i{width:22px;height:16px;border:2px solid #fff;display:block}

/* hero */
.hero{top:110px;height:640px;background:var(--beige)}
.hero .photo{left:80px;top:10px;width:1040px;height:590px;background:linear-gradient(120deg,#d7cfc4 0%,#b9342f 45%,#8f1f22 70%,#cbbfb0 100%)}
.hero-copy{position:absolute;left:120px;top:60px;z-index:2}
.hero-copy .lead{display:inline-block;background:var(--red);color:#fff;font-size:34px;font-weight:900;padding:4px 18px;transform:rotate(-4deg)}
.hero-copy h1{margin-top:18px;font-size:96px;font-weight:900;letter-spacing:.06em}
.hero-copy h1 span{background:#fff;padding:0 14px;margin-right:10px;box-shadow:6px 6px 0 var(--ink)}
.hero-link{margin-top:30px;display:inline-flex;gap:12px;align-items:center;background:#fff;padding:10px 16px;font-weight:700;font-size:18px}
.slider-arrows{position:absolute;right:40px;bottom:10px;display:flex;gap:24px;font-size:26px}

/* about */
.about{top:750px;height:740px;background:#fff}
.about .photo{left:0;top:30px;width:700px;height:620px;background:linear-gradient(180deg,#cfc9bf,#b3373a 55%,#9a9389)}
.about-word{position:absolute;left:470px;top:140px;writing-mode:vertical-rl;font-size:120px;font-weight:700;color:rgba(255,255,255,.55)}
.about-panel{position:absolute;left:660px;top:110px;width:540px;height:540px;background:var(--dark);color:#fff;padding:70px 60px}
.brand-tag{display:inline-block;background:var(--red);color:#fff;font-family:"Noto Sans JP",sans-serif;font-weight:700;font-size:18px;padding:4px 14px}
.about-panel h2{font-size:26px;margin:26px 0 28px}
.about-panel p{font-size:13px;line-height:2;color:#ccc}
.btn-outline{display:inline-block;margin-top:40px;border:1px solid #fff;padding:16px 60px;font-size:14px}

/* products */
.products{top:1490px;height:930px;background:#fff}
.products .band{position:absolute;left:160px;top:130px;width:1040px;height:620px;background:var(--sage)}
.products h2{position:absolute;left:300px;top:68px;font-size:30px;font-weight:900}
.products .bigword{position:absolute;left:640px;top:100px;font-size:140px;color:rgba(255,255,255,.3)}
.products .intro{position:absolute;left:650px;top:270px;width:460px;font-size:13px;line-height:2;color:#fff}
.card{position:absolute;background:#fff;width:300px;height:360px;border-left:30px solid var(--green)}
.card .tag{position:absolute;left:-30px;top:0;width:30px;color:#fff;font-size:11px;writing-mode:vertical-rl;padding:10px 8px}
.card .shot{position:absolute;left:30px;top:40px;width:210px;height:220px;background:linear-gradient(160deg,#d94b45,#a31d21)}
.card .name{position:absolute;right:16px;bottom:18px;display:flex;gap:10px;align-items:center;font-weight:700}
.card.c1{left:80px;top:230px}
.card.c2{left:400px;top:370px}
.card.c2 .shot{background:linear-gradient(160deg,#c9a27a,#b32a2c)}
.card.c3{left:760px;top:490px;width:340px}
.card.c3 .shot{width:260px;background:linear-gradient(160deg,#e8e8e8,#bbb)}

/* case study */
.cases{top:2420px;height:580px;background:var(--dark);color:#fff}
.cases h2{position:absolute;left:140px;top:60px;font-size:28px}
.cases .bigword{position:absolute;left:520px;top:20px;font-size:130px;color:rgba(255,255,255,.08)}
.case-arrows{position:absolute;right:60px;top:70px;display:flex;gap:8px}
.case-arrows span{width:32px;height:32px;background:#fff;color:var(--ink);display:flex;align-items:center;justify-content:center}
.case-card{position:absolute;top:160px;height:330px;background:#fff;color:var(--ink)}
.case-card .photo{top:0;height:100%}
.case-card .txt{position:absolute;padding:26px;font-size:13px;line-height:2}
.case-card h3{font-size:20px;margin-bottom:10px}
.case-a{left:0;width:260px}
.case-b{left:290px;width:700px}
.case-b .photo{left:0;width:320px;background:linear-gradient(135deg,#e2ddd6,#8c9aa6)}
.case-b .txt{left:330px}
.case-c{left:1020px;width:180px}
.case-c .photo{left:0;width:180px;background:linear-gradient(135deg,#eee,#bfc6c8)}
.company{display:block;text-align:right;margin-top:8px;font-weight:700}

/* news */
.news{top:3000px;height:540px;background:var(--beige)}
.news h2{position:absolute;left:110px;top:150px;font-size:28px}
.news .more{position:absolute;left:110px;top:230px;font-size:13px;display:flex;gap:10px;align-items:center}
.news ul{position:absolute;left:420px;top:110px;width:780px;list-style:none}
.news li{background:#fff;height:84px;margin-bottom:12px;padding:18px 80px 0 40px;position:relative;font-size:14px}
.news li time{display:block;font-size:11px;color:var(--muted);margin-bottom:6px}
.news li::after{content:"+";position:absolute;right:34px;top:26px;color:var(--green);font-size:24px}

/* banners */
.banners{top:3540px;height:360px;background:#fff}
.banner{position:absolute;top:40px;height:260px;width:580px}
.banner.faq{left:0;background:linear-gradient(135deg,#6a7a86,#a33236)}
.banner.corp{left:620px;background:linear-gradient(135deg,#8ea0b0,#4b5a66)}
.banner .label{position:absolute;left:100px;top:90px;color:#fff}
.banner.corp .label{left:auto;right:80px}
.banner h3{font-size:28px;margin-bottom:18px}
.banner .go{background:#fff;color:var(--ink);font-size:12px;padding:8px 20px;display:inline-flex;gap:10px;align-items:center}

/* contact */
.contact{top:3900px;height:440px;background:#fff}
.contact .photo{left:300px;top:40px;width:500px;height:360px;background:linear-gradient(90deg,#fff,#dfe4e8)}
.contact h2{position:absolute;left:90px;top:130px;font-size:28px}
.contact p{position:absolute;left:90px;top:190px;width:300px;font-size:13px;line-height:2}
.contact-btns{position:absolute;left:790px;top:80px;width:350px}
.contact-btns a{display:flex;align-items:center;gap:16px;height:86px;margin-bottom:14px;color:#fff;text-decoration:none;font-weight:700;padding:0 26px;background:var(--green)}
.contact-btns a.tel{font-size:30px}
.contact-btns a.tel small{font-size:13px}
.contact-btns svg{flex:none}

/* footer */
.site-footer{top:4340px;height:352px;background:#fff;border-top:1px solid var(--line)}
.site-footer .brand{top:70px;left:60px}
.f-info{position:absolute;left:60px;top:130px;font-size:12px;line-height:2}
.f-nav{position:absolute;left:360px;top:70px;display:flex;gap:80px;font-size:13px;line-height:2.3}
.f-nav ul{list-style:none}
.f-bottom{position:absolute;left:0;right:0;bottom:40px;display:flex;justify-content:space-between;padding:0 60px 0 560px;font-size:11px;color:var(--muted)}
</style>
</head>
<body>

<header class="site-header">
  <div class="brand"><span class="brand-mark"></span><div><small>株式会社</small>宝辺製作所</div></div>
  <ul class="gnav">
    <li>パロミクスについて<span>ABOUT</span></li>
    <li>製品一覧<span>PRODUCT</span></li>
    <li>導入事例<span>CASE STUDY</span></li>
    <li>会社概要<span>COMPANY</span></li>
  </ul>
  <div class="dropdown">パロミクス<br>逆パロミクス<br>オプションパーツ</div>
  <div class="header-cta">
    <a href="#"><i></i>見積依頼</a>
    <a href="#"><i></i>お問い合わせ</a>
  </div>
</header>

<section class="hero">
  <div class="photo" role="img" aria-label="倉庫内で赤いパロミクスに段ボール箱が積まれた写真"></div>
  <div class="hero-copy">
    <span class="lead">スペースを</span>
    <h1><span>有</span><span>効</span><span>活</span><span>用</span></h1>
    <div class="hero-link">パロミクスについて <span class="plus">+</span></div>
  </div>
  <div class="slider-arrows"><span>‹</span><span>›</span></div>
</section>

<section class="about">
  <div class="photo" role="img" aria-label="倉庫に並ぶ赤いパロミクスの写真"></div>
  <div class="about-word en">ABOUT</div>
  <div class="about-panel">
    <span class="brand-tag">PALOMIX</span>
    <h2>パロミクスについて</h2>
    <p>パロミクスとは、限られたスペースを有効に活用し、保管効率を高めるための積み重ね式の保管ラックシステムです。</p>
    <a class="btn-outline">詳しくはこちら　›</a>
  </div>
</section>

<section class="products">
  <div class="band"></div>
  <h2>製品一覧</h2>
  <div class="bigword en">PRODUCT</div>
  <p class="intro">上下段の荷を積み重ねることにより、倉庫内の空間を有効活用します。パレットを荷崩れから守り、安全な保管を実現します。用途に合わせてお選びいただけます。</p>
  <div class="card c1"><span class="tag en">PRODUCT</span><div class="shot" role="img" aria-label="赤いパロミクス製品の写真"></div><div class="name">パロミクス <span class="plus">+</span></div></div>
  <div class="card c2"><span class="tag en">PRODUCT</span><div class="shot" role="img" aria-label="段ボールを載せた逆パロミクスの写真"></div><div class="name">逆パロミクス <span class="plus">+</span></div></div>
  <div class="card c3"><span class="tag en">PRODUCT</span><div class="shot" role="img" aria-label="オプションパーツ各種の写真"></div><div class="name">オプションパーツ <span class="plus">+</span></div></div>
</section>

<section class="cases">
  <h2>導入事例</h2>
  <div class="bigword en">CASE STUDY</div>
  <div class="case-arrows"><span>‹</span><span>›</span></div>
  <div class="case-card case-a"><div class="txt">パロミクスを導入して、<br>課題が解消されました。<span class="company">F製造様</span></div></div>
  <div class="case-card case-b">
    <div class="photo" role="img" aria-label="倉庫で働く担当者の写真"></div>
    <div class="txt"><h3>便利に利用させて<br>いただいています。</h3><span class="company">T運送様</span>保管スペースの不足が解消され、作業の効率も大きく向上しました。<br>導入後も安心して使えています。</div>
  </div>
  <div class="case-card case-c"><div class="photo" role="img" aria-label="作業着の担当者の写真"></div></div>
</section>

<section class="news">
  <h2>お知らせ</h2>
  <div class="more">一覧を見る <span class="plus">+</span></div>
  <ul>
    <li><time>2022.03.01</time>新製品の取り扱いを開始しました。詳しくはこちらをご覧ください。</li>
    <li><time>2022.03.01</time>特価品キャンペーンを実施中です。在庫がなくなり次第終了します。</li>
    <li><time>2022.03.01</time>春季休業期間のお知らせです。期間中のお問い合わせについて。</li>
    <li><time>2022.03.01</time>ウェブサイトをリニューアルしました。今後ともよろしくお願いします。</li>
  </ul>
</section>

<section class="banners">
  <div class="banner faq" role="img" aria-label="倉庫ラックの写真"><div class="label"><h3>よくある質問</h3><span class="go">詳しくはこちら <span class="plus">+</span></span></div></div>
  <div class="banner corp" role="img" aria-label="会社社屋の外観写真"><div class="label"><h3>会社概要</h3><span class="go">詳しくはこちら <span class="plus">+</span></span></div></div>
</section>

<section class="contact">
  <div class="photo" role="img" aria-label="ヘッドセットを着けた問い合わせ窓口の写真"></div>
  <h2>お問い合わせ</h2>
  <p>パロミクスに関するご相談・ご質問・見積依頼などはお気軽にお問い合わせください。電話・メール（オンラインフォーム）より受け付けております。</p>
  <div class="contact-btns">
    <a class="tel" href="#"><svg width="30" height="30" viewBox="0 0 24 24"><path fill="#fff" d="M6.6 10.8a15 15 0 0 0 6.6 6.6l2.2-2.2a1 1 0 0 1 1-.25 11.4 11.4 0 0 0 3.6.57 1 1 0 0 1 1 1V20a1 1 0 0 1-1 1A17 17 0 0 1 3 4a1 1 0 0 1 1-1h3.5a1 1 0 0 1 1 1c0 1.25.2 2.45.57 3.57a1 1 0 0 1-.25 1z"/></svg><small>お電話は</small>0256-00-4821</a>
    <a href="#"><svg width="28" height="22" viewBox="0 0 28 22"><rect x="1" y="1" width="26" height="20" fill="none" stroke="#fff" stroke-width="2"/><path d="M1 1l13 11L27 1" fill="none" stroke="#fff" stroke-width="2"/></svg>メールでのお問い合わせはこちら</a>
    <a href="#"><svg width="24" height="28" viewBox="0 0 24 28"><rect x="1" y="1" width="22" height="26" fill="none" stroke="#fff" stroke-width="2"/><path d="M6 9h12M6 14h12M6 19h8" stroke="#fff" stroke-width="2"/></svg>見積依頼はこちら</a>
  </div>
</section>

<footer class="site-footer">
  <div class="brand"><span class="brand-mark"></span><div><small>株式会社</small>宝辺製作所</div></div>
  <div class="f-info">〒959-0000　新潟県燕北市中央町1-2-3<br>TEL. 0256-00-4821　FAX. 0256-00-4822</div>
  <div class="f-nav">
    <ul><li>パロミクスについて</li></ul>
    <ul><li>製品一覧</li><li>－パロミクス</li><li>－逆パロミクス</li><li>－オプションパーツ</li></ul>
    <ul><li>導入事例</li><li>よくある質問</li></ul>
    <ul><li>会社概要</li><li>お知らせ</li></ul>
    <ul><li>お問い合わせ</li><li>見積依頼</li></ul>
  </div>
  <div class="f-bottom"><span>プライバシーポリシー　サイトマップ</span><span>Copyright © HOBEN SEISAKUSHO All rights reserved.</span></div>
</footer>

</body>
</html>
```